WP website design (Bellwether)

We need a wordpress design for an established auction and real estate company based in Arkansas. The winning design will incorporate a professional color scheme with company logo in a clean layout. The design needs to consider that this will be developed on a responsive theme.

Industry/Entity Type

Real Estate

Font styles to use
Sans Serif

Colors

Designer to choose colors to be used in the design.

Requirements
Must have
• Site will have slideshow, please use stock real estate or other image. A rough idea of homepage content is attached - not necessarily for design purposes.

Navigation Structure is:
1) Home
2) Auctions
3) Services
4) For Sale
5) About Us
6) Reid Videos
7) News & Events
8) Contact Us

Widgets will include:
Social media icons (our page, Youtube, RSS)
Testimonials Widget - this should be prominent
Featured Video
Email Signup form (Sign up to receive exclusive email updates for Bellwether auctions. )
Nice to have
• A drop down menu example
Should not have
• no gavel in the design

```html
<!DOCTYPE html>
<html lang="en">
<head>
<meta charset="utf-8">
<title>Bellwether Auction &amp; Marketing</title>
<link href="https://fonts.googleapis.com/css2?family=Arimo:wght@400;700&display=swap" rel="stylesheet">
<style>
:root{
  --green:#0b8a3c;
  --green-dark:#087030;
  --ink:#1c1c1c;
  --text:#333;
  --muted:#777;
  --line:#e2e2e2;
  --panel:#f2f2f2;
  --nav:#222;
  --page:#fafafa;
}
*{margin:0;padding:0;box-sizing:border-box}
html,body{width:782px;height:1200px;overflow:hidden}
body{font-family:"Arimo",Arial,sans-serif;color:var(--text);background:var(--page);position:relative}
.abs{position:absolute}
.top-rule{left:0;top:0;width:782px;height:2px;background:var(--green)}
.hero-band{left:0;top:113px;width:782px;height:240px;background:linear-gradient(var(--green) 0%,#5fb883 40%,var(--page) 100%)}
.header{left:72px;top:4px;width:640px;height:81px;background:#fff}
.brand{left:14px;top:20px;color:var(--green-dark);font-weight:700}
.brand .name{font-size:28px;letter-spacing:1px;line-height:30px}
.brand .sub{font-size:11px;letter-spacing:.5px}
.follow{left:296px;top:21px;width:198px;height:35px;background:linear-gradient(#eee,#dcdcdc);border:1px solid #ccc;display:flex;align-items:center;padding-left:5px}
.follow .sq{width:22px;height:22px;background:#3b5998;margin-right:10px}
.follow b{display:block;font-weight:400;font-size:10px;color:#444}
.follow small{font-size:7.5px;color:#777}
.contact{right:14px;top:20px;text-align:right;font-size:7.5px;color:#333;line-height:12px}
.contact .who{font-size:12.5px;font-weight:700;color:var(--ink);line-height:18px}
.contact svg{vertical-align:middle;margin-right:4px}
.nav{left:72px;top:85px;width:640px;height:28px;background:linear-gradient(#333,#1a1a1a);display:flex;font-size:7.8px;font-weight:700;color:#fff}
.nav a{padding:0 11px;line-height:28px;color:#fff;text-decoration:none}
.nav a.current{background:var(--green)}
.nav .videos{margin-left:auto;background:var(--green);display:flex;align-items:center;gap:12px;padding:0 14px 0 20px}
.nav .videos span{width:18px;height:14px;background:#666;border:1px solid #888}
.slider{left:72px;top:124px;width:466px;height:233px;border:2px solid #fff;background:linear-gradient(120deg,#eef3ea 0%,#9fb98a 35%,#4a4a4a 55%,#d8c9a6 80%,#f0f0f0 100%)}
.pager{left:198px;top:205px;width:86px;height:26px;background:#fff;display:flex;align-items:center;justify-content:center;gap:6px;font-size:13px;font-weight:700;color:#222}
.pager i{width:4px;height:4px;border-radius:50%;background:#222;display:inline-block}
.pager i.on{background:var(--green)}
.portrait{left:550px;top:124px;width:160px;height:208px;background:linear-gradient(160deg,#e8f4ea 0%,#9cc4a4 40%,#3d4a5e 70%,#22283a 100%)}
.portrait-cap{left:550px;top:332px;width:160px;height:25px;background:var(--green);color:#fff;font-weight:700;font-size:11.5px;text-align:center;line-height:25px}
.testimonials{left:72px;top:360px;width:640px;height:90px;background:var(--panel);border-left:2px solid var(--green);text-align:center;padding:10px 26px 0}
.testimonials h2{font-size:12px;color:var(--ink);margin-bottom:10px}
.testimonials p{font-size:7.5px;line-height:12.5px;color:#333}
.testimonials .date{margin-top:8px}
.testimonials .quote{position:absolute;left:20px;top:20px;font-size:16px;font-weight:700;color:#333}
.section-title{font-size:12px;font-weight:700;color:var(--ink)}
.arrows{left:670px;top:468px;font-size:9px;color:#bbb;letter-spacing:6px}
.post{left:72px;width:640px;height:134px;background:#fff;border:1px solid var(--line)}
.thumb{position:absolute;left:14px;top:11px;width:140px;height:110px}
.post .body{position:absolute;left:174px;top:10px;width:452px}
.post h3{font-size:11.5px;font-weight:400;color:var(--ink);margin-bottom:10px}
.post p{font-size:7.5px;line-height:12.5px;color:#333}
.post .date{font-size:7.5px;margin-top:8px}
.meta{display:flex;align-items:center;gap:8px;margin-top:12px;font-size:8px;color:#888}
.meta .cat{color:#333;font-size:7.5px}
.meta svg{margin-right:3px;vertical-align:-2px}
.meta span{margin-right:5px}
.divider{left:72px;top:950px;width:640px;height:1px;background:var(--line)}
.video-text{left:86px;top:1003px;width:404px;font-size:7.5px;line-height:14.4px;color:#333}
.readmore{left:434px;top:1093px;width:56px;height:16px;background:#eee;border:1px solid #ddd;font-size:6.5px;color:#888;text-align:center;line-height:14px}
.readmore b{color:#d22}
.video-frame{left:512px;top:996px;width:198px;height:114px;border:2px solid #ddd;background:linear-gradient(#3a3a3a 0%,#6a5a50 40%,#8a6d5c 70%,#5a4a42 100%)}
.play{left:598px;top:1043px;width:26px;height:26px;border-radius:50%;background:rgba(255,255,255,.35)}
.footer{left:72px;top:1155px;width:640px;height:45px;background:#2a2a2a;color:#fff;display:flex;align-items:center;padding-left:14px;font-size:7.5px}
.footer .signup{margin-left:44px;font-size:9.5px;margin-right:18px}
.footer .field{width:180px;height:24px;background:#fff;color:#aaa;font-size:7.5px;line-height:24px;padding-left:11px}
.footer .go{width:28px;height:24px;background:var(--green);margin-left:4px;color:#fff;font-size:14px;font-weight:700;text-align:center;line-height:24px}
.footer .social{margin-left:auto;margin-right:14px;display:flex;gap:6px}
.footer .social i{width:13px;height:13px;border-radius:50%;background:#3a3a3a;display:block}
</style>
</head>
<body>
<div class="abs top-rule"></div>
<div class="abs hero-band"></div>

<header class="abs header">
  <div class="abs brand"><div class="name">BELLWETHER</div><div class="sub">AUCTION &amp; MARKETING, LLC</div></div>
  <div class="abs follow"><div class="sq"></div><div><b>Follow us on our page</b><small>Like us and keep up to date</small></div></div>
  <div class="abs contact">
    <div><svg width="9" height="7" viewBox="0 0 9 7"><path d="M0 2 Q4.5 -1 9 2 L8 3 L6 2.5 L6 3.5 L8 5 L8 7 L1 7 L1 5 L3 3.5 L3 2.5 L1 3Z" fill="#444"/></svg>+1 (555) 014 2290</div>
    <div class="who">Reid Hallorn</div>
    <div><svg width="10" height="7" viewBox="0 0 10 7"><rect x=".5" y=".5" width="9" height="6" fill="none" stroke="#444"/><path d="M.5 .5 L5 4 L9.5 .5" fill="none" stroke="#444"/></svg>reidhallorn@bellwether.com</div>
  </div>
</header>

<nav class="abs nav">
  <a class="current">Home</a><a>Auctions</a><a>Services</a><a>For Sale</a><a>About Us</a><a>News &amp; Events</a><a>Contact Us</a>
  <div class="videos">Reid Videos<span></span></div>
</nav>

<div class="abs slider" role="img" aria-label="Slideshow photo of three smiling business colleagues at an office desk">
  <div class="abs pager">❮ <i class="on"></i><i></i><i></i><i></i> ❯</div>
</div>
<div class="abs portrait" role="img" aria-label="Portrait of Reid Hallorn in a dark blazer and blue shirt"></div>
<div class="abs portrait-cap">Reid Hallorn</div>

<section class="abs testimonials">
  <span class="quote">“</span>
  <h2>Testimonials</h2>
  <p>Lorem ipsum dolor sit amet, consectetur adipiscing elit. Integer nec orci laoreet, ullamcorper sem eget, rutrum dui. Duis est dolor, interdum ut ligula sit amet, accumsan elementum libero. Lorem ipsum dolor sit amet, consectetur adipiscing elit. Integer ultricies quis ipsum consectetur vestibulum. C...</p>
  <p class="date">15 Dec 2014</p>
</section>

<h2 class="abs section-title" style="left:86px;top:467px">Current Auctions</h2>
<div class="abs arrows">‹ ›</div>

<article class="abs post" style="top:494px">
  <div class="thumb" role="img" aria-label="Photo of a person holding a skateboard on a city street" style="background:linear-gradient(100deg,#3a3a3a,#8a8a84 50%,#c8c8c2)"></div>
  <div class="body">
    <h3>Post with thumbnail</h3>
    <p>Lorem ipsum dolor sit amet, consectetur adipiscing elit. Integer nec orci laoreet, ullamcorper sem eget, rutrum dui. Duis est dolor, interdum ut ligula sit amet, accumsan elementum libero. Lorem ipsum dolor sit amet, consectetur adipiscing elit. Integer ultricies quis ipsum consectetur vestibulum. Lorem ipsum dolor sit amet, consectetur adipiscing elit. Integer nec orci laoreet, ullamcorper sem eget, rutrum dui. Duis est dolor, interdum ut ligula sit amet, accumsan elementum libero. Lorem ipsum dolor sit amet, consectetur</p>
    <p class="date">15 Dec 2014</p>
    <div class="meta">
      <svg width="10" height="7" viewBox="0 0 10 7"><ellipse cx="5" cy="3.5" rx="4.5" ry="3" fill="none" stroke="#888"/><circle cx="5" cy="3.5" r="1.3" fill="#888"/></svg><span>1831</span>
      <svg width="9" height="8" viewBox="0 0 9 8"><path d="M4.5 7.5 L1 4 A2 2 0 0 1 4.5 1.5 A2 2 0 0 1 8 4Z" fill="none" stroke="#888"/></svg><span>38</span>
      <svg width="9" height="8" viewBox="0 0 9 8"><ellipse cx="4.5" cy="3.5" rx="4" ry="3" fill="none" stroke="#888"/></svg><span>4</span>
      <svg width="9" height="7" viewBox="0 0 9 7"><path d="M.5 .5 H3.5 L4.5 1.5 H8.5 V6.5 H.5Z" fill="none" stroke="#888"/></svg><span class="cat">Post format, Uncategorized</span>
    </div>
  </div>
</article>

<article class="abs post" style="top:644px">
  <div class="thumb" role="img" aria-label="Photo of a city street with lit skyscrapers at dusk" style="background:linear-gradient(#8a8fb8,#6a5a78 50%,#2c3452)"></div>
  <div class="body">
    <h3>Standart post.</h3>
    <p>Lorem ipsum dolor sit amet, consectetur adipiscing elit. Integer nec orci laoreet, ullamcorper sem eget, rutrum dui. Duis est dolor, interdum ut ligula sit amet, accumsan elementum libero. Lorem ipsum dolor sit amet, consectetur adipiscing elit. Integer ultricies quis ipsum consectetur vestibulum. Lorem ipsum dolor sit amet, consectetur adipiscing elit. Integer nec orci laoreet, ullamcorper sem eget, rutrum dui. Duis est dolor, interdum ut ligula sit amet, accumsan elementum libero. Lorem ipsum dolor sit amet, consectetur</p>
    <p class="date">15 Dec 2014</p>
    <div class="meta">
      <svg width="10" height="7" viewBox="0 0 10 7"><ellipse cx="5" cy="3.5" rx="4.5" ry="3" fill="none" stroke="#888"/><circle cx="5" cy="3.5" r="1.3" fill="#888"/></svg><span>1831</span>
      <svg width="9" height="8" viewBox="0 0 9 8"><path d="M4.5 7.5 L1 4 A2 2 0 0 1 4.5 1.5 A2 2 0 0 1 8 4Z" fill="none" stroke="#888"/></svg><span>38</span>
      <svg width="9" height="8" viewBox="0 0 9 8"><ellipse cx="4.5" cy="3.5" rx="4" ry="3" fill="none" stroke="#888"/></svg><span>4</span>
      <svg width="9" height="7" viewBox="0 0 9 7"><path d="M.5 .5 H3.5 L4.5 1.5 H8.5 V6.5 H.5Z" fill="none" stroke="#888"/></svg><span class="cat">Post format, Uncategorized</span>
    </div>
  </div>
</article>

<article class="abs post" style="top:794px">
  <div class="thumb" role="img" aria-label="Photo of a suspension bridge and city skyline at sunset" style="background:linear-gradient(#e8b88a,#c9a48c 45%,#6a7a98 75%,#3c4a6a)"></div>
  <div class="body">
    <h3>Half Up Half Down Hairstyles</h3>
    <p>Lorem ipsum dolor sit amet, consectetur adipiscing elit. Integer nec orci laoreet, ullamcorper sem eget, rutrum dui. Duis est dolor, interdum ut ligula sit amet, accumsan elementum libero. Lorem ipsum dolor sit amet, consectetur adipiscing elit. Integer ultricies quis ipsum consectetur vestibulum. Lorem ipsum dolor sit amet, consectetur adipiscing elit. Integer nec orci laoreet, ullamcorper sem eget, rutrum dui. Duis est dolor, interdum ut ligula sit amet, accumsan elementum libero. Lorem ipsum dolor sit amet, consectetur</p>
    <p class="date">15 Dec 2014</p>
    <div class="meta">
      <svg width="10" height="7" viewBox="0 0 10 7"><ellipse cx="5" cy="3.5" rx="4.5" ry="3" fill="none" stroke="#888"/><circle cx="5" cy="3.5" r="1.3" fill="#888"/></svg><span>1831</span>
      <svg width="9" height="8" viewBox="0 0 9 8"><path d="M4.5 7.5 L1 4 A2 2 0 0 1 4.5 1.5 A2 2 0 0 1 8 4Z" fill="none" stroke="#888"/></svg><span>38</span>
      <svg width="9" height="8" viewBox="0 0 9 8"><ellipse cx="4.5" cy="3.5" rx="4" ry="3" fill="none" stroke="#888"/></svg><span>4</span>
      <svg width="9" height="7" viewBox="0 0 9 7"><path d="M.5 .5 H3.5 L4.5 1.5 H8.5 V6.5 H.5Z" fill="none" stroke="#888"/></svg><span class="cat">Post format, Uncategorized</span>
    </div>
  </div>
</article>

<div class="abs divider"></div>

<h2 class="abs section-title" style="left:86px;top:979px">Featured Video</h2>
<p class="abs video-text">Lorem ipsum dolor sit amet, consectetur adipiscing elit, sed do eiusmod tempor incididunt ut labore et dolore magna aliqua. Ut enim ad minim veniam, quis nostrud exercitation ullamco laboris nisi ut aliquip ex eaLorem ipsum dolor sit amet, consectetur adipiscing elit, sed do eiusmod tempor incididunt ut labore et dolore magna aliqua. Ut enim ad minim veniam, quis nostrud exercitation ullamco laboris nisi ut aliquip ex eaLorem ipsum dolor sit amet, consectetur adipiscing elit, sed do eiusmod tempor incididunt ut labore et dolore magna aliqua. Ut enim ad minim veniam, quis nostrud exercitation ullamco laboris nisi ut aliquip ex ea</p>
<div class="abs readmore">Read More <b>»</b></div>
<div class="abs video-frame" role="img" aria-label="Video still of a packed auction hall audience"></div>
<svg class="abs play" viewBox="0 0 26 26"><circle cx="13" cy="13" r="12" fill="rgba(255,255,255,.35)"/><path d="M11 8 L16 13 L11 18" fill="none" stroke="#fff" stroke-width="2"/></svg>

<footer class="abs footer">
  <span>Copyright © 2014 bellwether. All Rights Reserved.</span>
  <span class="signup">Sign up</span>
  <div class="field">Enter Email</div>
  <div class="go">❯</div>
  <div class="social"><i></i><i></i><i></i><i></i></div>
</footer>
</body>
</html>
```